Tarvil GmbH business card

We Tarvil GmbH based in Switzerland are looking for a business card design. The Fresh Jung, appealing to customers of all kinds. We already have a logo to upload but still a business card. Details: Tarvil GmbH Address: Lindenweg 14b in 9412 Rudolfen. Tel: 41 76 392 00 47, web: Tarvil.ch, E-mail: info@Tarvil.ch Facebook: Tarvil GmbH. I am the Managing Director: Lukas Verholt. On reverse: Title: Transporter and bus rental Gross: Without deposit Super prices
Contact Information for Business Card
Siehe Projektbeschreibung
Requirements
Should not have
- Other pictures

```html
<!DOCTYPE html>
<html lang="de">
<head>
<meta charset="utf-8">
<title>Tarvil GmbH – Visitenkarte</title>
<link rel="stylesheet" href="https://fonts.googleapis.com/css2?family=Lato:ital,wght@0,300;0,400;0,700;0,900;1,300&display=swap">
<style>
  :root {
    --navy: #0b0b80;
    --ink: #1d1d2b;
    --paper: #ffffff;
    --backdrop: #e9e7e3;
  }
  * { margin: 0; padding: 0; box-sizing: border-box; }
  html, body { width: 1200px; height: 901px; overflow: hidden; }
  body {
    background: var(--backdrop);
    font-family: "Lato", sans-serif;
    display: flex;
    align-items: center;
    justify-content: center;
    gap: 40px;
  }
  .card {
    width: 540px;
    height: 340px;
    position: relative;
    box-shadow: 0 6px 18px rgba(0,0,0,0.18);
  }
  /* Front side */
  .card-front { background: var(--paper); color: var(--ink); }
  .brand {
    position: absolute;
    left: 36px; top: 96px;
    display: flex; align-items: center; gap: 10px;
  }
  .brand-mark { width: 26px; height: 26px; background: var(--navy); flex: none; }
  .brand-name {
    font-weight: 900; font-size: 24px; letter-spacing: 0.5px;
    color: var(--navy); white-space: nowrap;
  }
  .divider {
    position: absolute;
    left: 290px; top: 56px;
    width: 1.5px; height: 180px;
    background: var(--navy);
  }
  .contact {
    position: absolute;
    left: 316px; top: 104px;
  }
  .person-name {
    font-weight: 900; font-size: 24px; color: var(--navy); line-height: 1.1;
    white-space: nowrap;
  }
  .person-role { font-size: 16px; margin-top: 2px; margin-bottom: 10px; }
  .contact-list { list-style: none; }
  .contact-list li {
    display: flex; align-items: center; gap: 10px;
    font-size: 16px; line-height: 23px; white-space: nowrap;
  }
  .contact-list svg { width: 14px; height: 14px; flex: none; fill: var(--navy); }
  .address {
    position: absolute;
    left: 36px; bottom: 36px;
    font-size: 17px; white-space: nowrap;
  }
  /* Back side */
  .card-back {
    background: var(--navy); color: var(--paper);
    display: flex; flex-direction: column; align-items: center; justify-content: center;
    text-align: center;
  }
  .headline { font-weight: 700; font-size: 40px; line-height: 1.2; }
  .tagline { font-weight: 300; font-style: italic; font-size: 22px; margin-top: 22px; }
</style>
</head>
<body>
  <section class="card card-front" aria-label="Vorderseite">
    <div class="brand">
      <span class="brand-mark"></span>
      <span class="brand-name">Tarvil GmbH</span>
    </div>
    <div class="divider"></div>
    <div class="contact">
      <p class="person-name">Lukas Verholt</p>
      <p class="person-role">Geschäftsführer</p>
      <ul class="contact-list">
        <li>
          <svg viewBox="0 0 24 24" aria-hidden="true"><path d="M6.6 10.8a15.1 15.1 0 0 0 6.6 6.6l2.2-2.2a1 1 0 0 1 1-.25 11.4 11.4 0 0 0 3.6.57 1 1 0 0 1 1 1V20a1 1 0 0 1-1 1A17 17 0 0 1 3 4a1 1 0 0 1 1-1h3.5a1 1 0 0 1 1 1c0 1.25.2 2.45.57 3.570a1 1 0 0 1-.25 1z"/></svg>
          +41 76 392 00 47
        </li>
        <li>
          <svg viewBox="0 0 24 24" aria-hidden="true"><path d="M2 5h20v14H2z M2 5l10 8 10-8" fill="none" stroke="#0b0b80" stroke-width="2"/></svg>
          info@Tarvil.ch
        </li>
        <li>
          <svg viewBox="0 0 24 24" aria-hidden="true"><g fill="none" stroke="#0b0b80" stroke-width="2"><circle cx="12" cy="12" r="10"/><ellipse cx="12" cy="12" rx="4.5" ry="10"/><path d="M2 12h20"/></g></svg>
          www.Tarvil.ch
        </li>
        <li>
          <svg viewBox="0 0 24 24" aria-hidden="true"><rect x="2" y="2" width="20" height="20" rx="2"/></svg>
          /Tarvil-GmbH
        </li>
      </ul>
    </div>
    <p class="address">Lindenweg 14b, 9412 Rudolfen</p>
  </section>

  <section class="card card-back" aria-label="Rückseite">
    <h1 class="headline">Ohne Kaution<br>Super Preise</h1>
    <p class="tagline">Transporter und Bus Vermietung</p>
  </section>
</body>
</html>
```